Shopify Theme design for a Subscription Cyber security service for consumers and SMB

Looking for the Theme design for our shopify store that will be selling a Cyber Security subscription service to Consumers and SMB. The service provides enterprise grade tools at consumer prices.
we have logos and colour scheme ready to go, however we don't use 2, 4, 7 or 8 typically in what we do.
it will be a pretty simple shop and it will be using the subscriptions app from shopify also.
We will need all the standard pages such as:
the home page
pages
Product/Subscription page
Cart
404
And any others that are standard in a theme that I have not listed
Cyber Security
Coded - Design and coding required
4 page

```html
<!DOCTYPE html>
<html lang="en">
<head>
<meta charset="utf-8">
<title>Vantaguard – Cyber Security Subscriptions</title>
<link href="https://fonts.googleapis.com/css2?family=Poppins:wght@300;400;500;600;700&display=swap" rel="stylesheet">
<style>
:root{
  --blue:#4583e3;
  --blue-deep:#2f5fc4;
  --magenta:#a3216e;
  --magenta-dark:#8c1b5e;
  --ice:#eaf4fc;
  --ink:#1e1e24;
  --text:#3d3d45;
  --white:#ffffff;
}
*{margin:0;padding:0;box-sizing:border-box}
html,body{width:1200px;height:4335px;overflow:hidden}
body{position:relative;font-family:'Poppins',sans-serif;color:var(--text);background:var(--white)}
.abs{position:absolute}
a{color:inherit;text-decoration:none}

/* header */
.site-header{top:0;left:0;width:1200px;height:84px;background:var(--white)}
.brand{display:flex;align-items:center;gap:10px;font-size:24px;letter-spacing:2px;font-weight:400}
.brand-mark{width:26px;height:26px;border-radius:50%}
.site-header .brand{left:111px;top:24px;color:var(--blue-deep)}
.brand-mark.dark{background:var(--blue-deep)}
.main-nav{left:459px;top:30px;display:flex;gap:33px;font-size:15px;color:var(--ink)}
.nav-search{left:912px;top:32px}
.btn{display:flex;align-items:center;justify-content:center;border:2px solid var(--magenta);border-radius:6px;font-size:14px;color:var(--ink);background:var(--white)}
.header-cta{left:958px;top:22px;width:133px;height:41px}

/* hero */
.hero{top:84px;left:0;width:1200px;height:598px;background:linear-gradient(120deg,#2f63c9 0%,#3e7be0 55%,#2b5cc0 100%);clip-path:polygon(0 0,100% 0,100% 547px,0 598px)}
.hero-photo{left:631px;top:34px;width:446px;height:538px;background:linear-gradient(180deg,rgba(255,255,255,.18),rgba(20,30,60,.35));border-radius:4px}
.hero-eyebrow{left:109px;top:230px;font-size:25px;color:var(--white);font-weight:400}
.hero-title{left:106px;top:270px;font-size:54px;color:var(--white);font-weight:700;letter-spacing:1px}
.hero-text{left:109px;top:350px;width:492px;font-size:15.5px;line-height:27px;color:var(--white);text-align:justify}

/* section heads */
.eyebrow{font-size:22px;color:var(--magenta);font-weight:500}
.heading{font-size:37px;color:var(--blue);font-weight:600;line-height:48px}
.center{left:0;width:1200px;text-align:center}

/* features */
.card{background:var(--white);box-shadow:0 4px 18px rgba(0,0,0,.13)}
.feature{top:942px;width:305px;height:287px;text-align:center}
.feature svg{margin-top:26px}
.feature h3{font-size:22px;color:var(--blue);font-weight:600;margin-top:10px}
.feature p{font-size:14px;line-height:21px;margin:12px 20px 0;color:var(--text)}
.feature::after{content:"";position:absolute;left:24px;right:24px;bottom:0;height:7px;background:var(--magenta)}

/* about */
.about{top:1316px;left:0;width:1200px;height:581px;background:var(--ice)}
.about-photo{left:84px;top:56px;width:438px;height:525px;background:linear-gradient(160deg,#d6e6f5,#9fb4cc);border-radius:4px}
.about-copy{left:576px;top:80px;width:515px}
.about-copy .heading{margin-top:14px;text-align:justify}
.about-copy p{margin-top:22px;font-size:15.5px;line-height:25.6px;text-align:justify}
.about-copy .btn{margin-top:30px;width:167px;height:40px}

/* pricing */
.pricing{top:1897px;left:0;width:1200px;height:858px;background:radial-gradient(circle at 30% 40%,#b02a7a,var(--magenta) 60%,var(--magenta-dark))}
.pricing .eyebrow,.pricing .heading{color:var(--white)}
.toggle{left:476px;top:207px;width:248px;height:38px;display:flex;border-radius:4px;overflow:hidden;border:2px solid var(--white);font-size:14px}
.toggle span{flex:1;display:flex;align-items:center;justify-content:center}
.toggle .on{background:var(--blue);color:var(--white)}
.toggle .off{background:var(--ice);color:var(--ink)}
.plan{top:296px;width:305px;height:475px;text-align:center;border-top:7px solid var(--blue)}
.plan h3{font-size:25px;color:var(--ink);font-weight:600;margin-top:36px}
.price{margin:28px auto 0;width:197px;height:47px;border:1.5px solid #8a8a8a;border-radius:24px;display:flex;align-items:center;justify-content:center;gap:6px;font-size:14px;color:var(--ink)}
.price b{color:var(--magenta);font-size:18px;font-weight:600}
.plan ul{list-style:none;margin-top:26px;font-size:15px;line-height:32px;color:var(--ink)}
.plan .btn{margin:28px auto 0;width:167px;height:40px}

/* faq */
.faq{top:2755px;left:0;width:1200px;height:675px;background:var(--ice)}
.faq .eyebrow{left:111px;top:82px}
.faq .heading{left:111px;top:122px;font-size:38px}
.faq-line{left:134px;top:258px;height:250px;border-left:2px dotted #b9c5d4}
.faq-item{left:111px;width:520px}
.q-pin{position:absolute;left:0;top:0;width:47px;height:52px}
.faq-item h4{position:absolute;left:69px;top:10px;font-size:17px;font-weight:500;color:var(--ink);white-space:nowrap}
.faq-item p{position:absolute;left:69px;top:46px;width:430px;font-size:14px;line-height:22px}
.faq-art{left:673px;top:207px;width:418px;height:253px;background:radial-gradient(ellipse at center,#ffffff 0%,#dcebf8 70%,rgba(234,244,252,0) 100%);border-radius:12px}

/* join */
.join .heading{top:3510px;font-size:40px}
.join-text{left:150px;width:900px;text-align:center;font-size:15px;line-height:26px}
.join .btn{left:515px;top:3775px;width:168px;height:39px}

/* footer */
.site-footer{top:3905px;left:0;width:1200px;height:378px;background:radial-gradient(circle at 70% 50%,#b02a7a,var(--magenta) 60%,var(--magenta-dark));clip-path:polygon(0 42px,100% 0,100% 100%,0 100%)}
.site-footer .brand{left:111px;top:146px;color:var(--white)}
.brand-mark.light{background:var(--white)}
.footer-about{left:111px;top:208px;width:290px;font-size:15px;line-height:26px;color:var(--white);text-align:justify}
.social{left:111px;top:320px;display:flex;gap:14px}
.social span{width:18px;height:18px;border-radius:50%;background:var(--white)}
.footer-col{top:148px;color:var(--white)}
.footer-col h5{font-size:19px;font-weight:600}
.footer-col ul{list-style:none;margin-top:10px;font-size:14px;line-height:26px}
.footer-col li::before{content:"›";margin-right:7px;font-size:18px}
.copyright{top:4283px;left:0;width:1200px;height:52px;background:var(--blue);color:var(--white);font-size:15px;display:flex;align-items:center;justify-content:center}
</style>
</head>
<body>

<header class="site-header abs">
  <div class="brand abs"><span class="brand-mark dark"></span>VANTAGUARD</div>
  <nav class="main-nav abs"><a>Benefits</a><a>Scope Of Work</a><a>Pricing</a><a>FAQ</a><a>Blog</a></nav>
  <svg class="nav-search abs" width="17" height="17" viewBox="0 0 17 17" fill="none" stroke="#1e1e24" stroke-width="2"><circle cx="7" cy="7" r="5"/><path d="M11 11l4.5 4.5"/></svg>
  <a class="btn header-cta abs">Get Started</a>
</header>

<section class="hero abs">
  <div class="hero-photo abs" role="img" aria-label="Smiling security specialist with arms crossed in front of a server room"></div>
  <p class="hero-eyebrow abs">WELCOME TO</p>
  <h1 class="hero-title abs">VANTAGUARD</h1>
  <p class="hero-text abs">Lorem ipsum dolor sit amet, consectetur adipiscing elit, sed do eiusmod tempor incididunt ut labore et dolore magna aliqua. Quis ipsum suspendisse ultrices gravida. Risus commodo viverra maecenas accumsan</p>
</section>

<section class="features">
  <p class="eyebrow abs center" style="top:757px">Vantaguard Features</p>
  <h2 class="heading abs center" style="top:800px">Precious Features Included<br>With Vantaguard</h2>

  <article class="card feature abs" style="left:111px">
    <svg width="100" height="100" viewBox="0 0 100 100" fill="none" stroke="#111" stroke-width="3"><circle cx="50" cy="50" r="22"/><rect x="41" y="48" width="18" height="14" rx="2"/><path d="M44 48v-5a6 6 0 0112 0v5"/><path d="M28 40H14M28 60H14M72 40h14M72 60h14M40 28V14M60 28V14M40 72v14M60 72v14"/><circle cx="10" cy="40" r="4"/><circle cx="10" cy="60" r="4"/><circle cx="90" cy="40" r="4"/><circle cx="90" cy="60" r="4"/><circle cx="40" cy="10" r="4"/><circle cx="60" cy="10" r="4"/><circle cx="40" cy="90" r="4"/><circle cx="60" cy="90" r="4"/></svg>
    <h3>Lorem ipsum dolor</h3>
    <p>Lorem ipsum dolor sit amet, consectetur adipiscing elit, sed do eiusmod tempor incididunt ut labore</p>
  </article>
  <article class="card feature abs" style="left:448px">
    <svg width="100" height="100" viewBox="0 0 100 100" fill="none" stroke="#111" stroke-width="3"><path d="M50 10l32 12v22c0 22-14 38-32 46C32 82 18 66 18 44V22z"/><path d="M50 18l25 9v18c0 17-11 30-25 37-14-7-25-20-25-37V27z"/><rect x="39" y="48" width="22" height="18" rx="2"/><path d="M43 48v-6a7 7 0 0114 0v6"/></svg>
    <h3>Lorem ipsum dolor</h3>
    <p>Lorem ipsum dolor sit amet, consectetur adipiscing elit, sed do eiusmod tempor incididunt ut labore</p>
  </article>
  <article class="card feature abs" style="left:784px">
    <svg width="100" height="100" viewBox="0 0 100 100" fill="none" stroke="#111" stroke-width="3"><rect x="14" y="30" width="72" height="46" rx="3"/><path d="M6 82h88l-4 6H10z"/><path d="M50 8l24 9v16c0 17-10 29-24 35-14-6-24-18-24-35V17z" fill="#fff"/><path d="M40 36l7 7 14-14"/></svg>
    <h3>Lorem ipsum dolor</h3>
    <p>Lorem ipsum dolor sit amet, consectetur adipiscing elit, sed do eiusmod tempor incididunt ut labore</p>
  </article>
</section>

<section class="about abs">
  <div class="about-photo abs" role="img" aria-label="Security analyst holding a laptop in front of a faint shield graphic"></div>
  <div class="about-copy abs">
    <p class="eyebrow">About Vantaguard</p>
    <h2 class="heading">Sed ut perspiciatis unde omnis iste natus error</h2>
    <p>Lorem ipsum dolor sit amet, consectetur adipiscing elit, sed do eiusmod tempor incididunt ut labore et dolore magna aliqua. Ut enim ad minim veniam, quis nostrud exercitation ullamco laboris nisi ut aliquip ex ea commodo consequat. Duis aute irure dolor in reprehenderit in voluptate velit esse cillum dolore eu fugiat nulla pariatur. Excepteur sint occaecat cupidatat non proident, sunt in culpa qui officia deserunt mollit anim id est laborum.</p>
    <a class="btn">Learn More</a>
  </div>
</section>

<section class="pricing abs">
  <p class="eyebrow abs center" style="top:77px">Vantaguard Price</p>
  <h2 class="heading abs center" style="top:118px">Simple And Flexible Pricing</h2>
  <div class="toggle abs"><span class="on">Monthly</span><span class="off">Yearly</span></div>

  <article class="plan card abs" style="left:111px">
    <h3>Standard</h3>
    <div class="price"><b>Free /</b> Per Month</div>
    <ul><li>Sed Ut Perspiciatis Unde Omnis</li><li>Lorem Ipsum Dolor</li><li>Natus Error Sit Voluptatem</li><li>Sed Ut Perspiciatis Unde</li><li>Ut Enim Ad Minima</li><li>Lorem Ipsum Dolor Consect</li></ul>
    <a class="btn">Purchase Now</a>
  </article>
  <article class="plan card abs" style="left:448px">
    <h3>Popular</h3>
    <div class="price"><b>$45 /</b> Per Month</div>
    <ul><li>Sed Ut Perspiciatis Unde Omnis</li><li>Lorem Ipsum Dolor</li><li>Natus Error Sit Voluptatem</li><li>Sed Ut Perspiciatis Unde</li><li>Ut Enim Ad Minima</li><li>Lorem Ipsum Dolor Consect</li></ul>
    <a class="btn">Purchase Now</a>
  </article>
  <article class="plan card abs" style="left:784px">
    <h3>Premium</h3>
    <div class="price"><b>$76 /</b> Per Month</div>
    <ul><li>Sed Ut Perspiciatis Unde Omnis</li><li>Lorem Ipsum Dolor</li><li>Natus Error Sit Voluptatem</li><li>Sed Ut Perspiciatis Unde</li><li>Ut Enim Ad Minima</li><li>Lorem Ipsum Dolor Consect</li></ul>
    <a class="btn">Purchase Now</a>
  </article>
</section>

<section class="faq abs">
  <p class="eyebrow abs">General Questions</p>
  <h2 class="heading abs">Frequently Asked Questions</h2>
  <div class="faq-line abs"></div>

  <div class="faq-item abs" style="top:210px">
    <svg class="q-pin" viewBox="0 0 47 52"><path d="M23.5 2a21.5 21.5 0 0110 40.5L23.5 51l-10-8.5A21.5 21.5 0 0123.5 2z" fill="#a3216e"/><text x="23.5" y="30" text-anchor="middle" font-family="Poppins,sans-serif" font-size="22" font-weight="600" fill="#fff">?</text></svg>
    <h4>Lorem ipsum dolor sit amet, consectetur adipis ?</h4>
    <p>Lorem ipsum dolor sit amet, consectetur adipiscing elit, sed do eiusmod tempor incididunt ut labore et dolore magna aliqua. Quis ipsum suspendisse</p>
  </div>
  <div class="faq-item abs" style="top:360px">
    <svg class="q-pin" viewBox="0 0 47 52"><path d="M23.5 2a21.5 21.5 0 0110 40.5L23.5 51l-10-8.5A21.5 21.5 0 0123.5 2z" fill="#a9a9ad"/><text x="23.5" y="30" text-anchor="middle" font-family="Poppins,sans-serif" font-size="22" font-weight="600" fill="#fff">?</text></svg>
    <h4>Lorem ipsum dolor sit amet, consectetur adipis ?</h4>
  </div>
  <div class="faq-item abs" style="top:444px">
    <svg class="q-pin" viewBox="0 0 47 52"><path d="M23.5 2a21.5 21.5 0 0110 40.5L23.5 51l-10-8.5A21.5 21.5 0 0123.5 2z" fill="#a9a9ad"/><text x="23.5" y="30" text-anchor="middle" font-family="Poppins,sans-serif" font-size="22" font-weight="600" fill="#fff">?</text></svg>
    <h4>Lorem ipsum dolor sit amet, consectetur adipis ?</h4>
  </div>
  <div class="faq-item abs" style="top:528px">
    <svg class="q-pin" viewBox="0 0 47 52"><path d="M23.5 2a21.5 21.5 0 0110 40.5L23.5 51l-10-8.5A21.5 21.5 0 0123.5 2z" fill="#a9a9ad"/><text x="23.5" y="30" text-anchor="middle" font-family="Poppins,sans-serif" font-size="22" font-weight="600" fill="#fff">?</text></svg>
    <h4>Lorem ipsum dolor sit amet, consectetur adipis ?</h4>
  </div>

  <div class="faq-art abs" role="img" aria-label="Three white speech bubbles with blue question marks"></div>
</section>

<section class="join">
  <h2 class="heading abs center">Ready to Join?</h2>
  <p class="join-text abs" style="top:3598px">Lorem ipsum dolor sit amet, consectetur adipiscing elit, sed do eiusmod tempor incididunt ut labore et dolore magna aliqua. Ut enim ad minim veniam, quis nostrud exercitation ullamco laboris nisi ut aliquip ex ea commodo consequat. Duis aute irure dolor in reprehenderit in voluptate velit esse cillum dolore eu</p>
  <p class="join-text abs" style="top:3693px">fugiat nulla pariatur. Excepteur sint occaecat cupidatat non proident, sunt in culpa qui officia deserunt mollit anim id est laborum.</p>
  <a class="btn abs">Get Started</a>
</section>

<footer class="site-footer abs">
  <div class="brand abs"><span class="brand-mark light"></span>VANTAGUARD</div>
  <p class="footer-about abs">Lorem ipsum dolor sit amet, consectetur adipiscing elit, sed do eiusmod tempor incididunt ut labore et dolore magna aliqua</p>
  <div class="social abs" aria-label="Social profiles"><span></span><span></span><span></span></div>
  <div class="footer-col abs" style="left:483px"><h5>Cyber Services</h5><ul><li>Our Services</li><li>Presale Service</li><li>Partner</li><li>Career</li></ul></div>
  <div class="footer-col abs" style="left:707px"><h5>Support &amp; Help</h5><ul><li>About Us</li><li>Blog</li><li>FAQ's</li><li>Contact Us</li></ul></div>
  <div class="footer-col abs" style="left:931px"><h5>Quick Links</h5><ul><li>Pricing</li><li>Our Team</li><li>Privacy Policy</li><li>Terms &amp; Conditions</li></ul></div>
</footer>
<div class="copyright abs">Copyright © 2024 Vantaguard. All rights reserved.</div>

</body>
</html>
```